Book Cover for: TITLE Mend the Quiet Hours SUBTITLE For couples who don't want to break up

We need a full cover design for a book on relationships written by husband and wife team, Marla and Walter Dunmore, PhD. This book will offer hope for couples that are on the verge of breaking up but want to work things out and stay together. The theme is to teach couples about their own reactions to their partner, how moods affect a relationship, how to get creative to solving problems and how to have a good feeling towards your partner regardless of differences. This book is about hope. It is a positive look at relationships that feel hopeless.

Target Market(s)

Married or couples that are going through a difficult time and are considering splitting up due to, communication difficulties, addiction, affair. We imagine the book will appeal to women more than men but still want a cover that men would be comfortable picking up.

Colors

Designer to choose colors to be used in the design.

Requirements
Must have
• We want the cover to beautiful, intriguing, simple and uncomplicated. We don't want it overly busy, technical, or complex.
Nice to have
• MAYBE?? a broken heart being put back together.
Should not have
• No photo, no cartoon, no flowers, no couple (unless obscure and not gender specific).

```html
<!DOCTYPE html>
<html lang="en">
<head>
<meta charset="UTF-8">
<title>Mend the Quiet Hours — Cover Variants</title>
<link rel="stylesheet" href="https://fonts.googleapis.com/css2?family=Open+Sans:wght@700;800&family=EB+Garamond:wght@600&display=swap">
<style>
  :root {
    --backdrop: #c4c4c4;
    --ink-dark: #050607;
    --paper-light: #f2f2f2;
    --paper-shade: #e6e6e6;
    --pink: #eda8cc;
    --white: #ffffff;
    --red: #ec1c3c;
    --blue: #1e93bf;
  }
  * { margin: 0; padding: 0; box-sizing: border-box; }
  html, body { width: 1200px; height: 704px; overflow: hidden; }
  body {
    background: var(--backdrop);
    position: relative;
    font-family: "Open Sans", Arial, sans-serif;
  }
  .cover {
    position: absolute;
    top: 112px;
    width: 334px;
    height: 455px;
  }
  .cover--night { left: 210px; background: var(--ink-dark); }
  .cover--day {
    left: 640px;
    background: linear-gradient(160deg, var(--paper-light), var(--paper-shade));
  }
  .title-main, .title-sub, .tagline-line, .authors { position: absolute; white-space: nowrap; }
  .title-main {
    left: 38px; top: 35px;
    font-size: 46px; font-weight: 700; line-height: 1;
    letter-spacing: 0.13em;
  }
  .title-sub {
    left: 38px; top: 91px;
    font-size: 22px; font-weight: 700; line-height: 1;
    letter-spacing: 0.57em;
  }
  .hearts {
    position: absolute; left: 34px; top: 144px;
    width: 272px; height: 64px;
    display: flex; justify-content: space-between; align-items: flex-start;
  }
  .heart-slot { width: 56px; height: 60px; border-radius: 6px; }
  .tagline-line {
    font-size: 17px; font-weight: 700; line-height: 1;
    letter-spacing: 0.2em;
  }
  .tagline-line--one { left: 43px; top: 246px; }
  .tagline-line--two { left: 93px; top: 269px; }
  .tagline-line--three { left: 170px; top: 292px; }
  .emphasis { position: relative; }
  .cover--night .emphasis::after {
    content: ""; position: absolute; left: 0; right: 0.2em; bottom: -5px;
    height: 2px; border-radius: 2px; background: var(--pink);
  }
  .authors {
    left: 0; right: 0; top: 373px;
    text-align: center; padding-left: 20px;
    font-family: "EB Garamond", Georgia, serif;
    font-size: 18px; font-weight: 600; line-height: 23px;
    letter-spacing: 0.2em;
  }
  .cover--night .title-main { color: var(--pink); }
  .cover--night .title-sub,
  .cover--night .tagline-line,
  .cover--night .authors { color: var(--white); }
  .cover--night .heart-slot { background: var(--white); }
  .cover--night .heart-slot--whole { background: var(--pink); }
  .cover--day .title-main,
  .cover--day .emphasis,
  .cover--day .authors { color: var(--red); }
  .cover--day .title-sub,
  .cover--day .tagline-line { color: var(--blue); }
  .cover--day .heart-slot { background: var(--red); }
</style>
</head>
<body>
  <section class="cover cover--night">
    <h1>
      <span class="title-main">MEND THE</span>
      <span class="title-sub">QUIET HOURS</span>
    </h1>
    <div class="hearts">
      <div class="heart-slot" role="img" aria-label="Heart shattered into many pieces"></div>
      <div class="heart-slot" role="img" aria-label="Heart with pieces drawing back together"></div>
      <div class="heart-slot" role="img" aria-label="Heart whole with faint cracks"></div>
      <div class="heart-slot heart-slot--whole" role="img" aria-label="Fully mended heart"></div>
    </div>
    <p class="tagline">
      <span class="tagline-line tagline-line--one">For couples</span>
      <span class="tagline-line tagline-line--two">who <span class="emphasis">don't</span> want</span>
      <span class="tagline-line tagline-line--three">to break up</span>
    </p>
    <p class="authors">MARLA &amp; WALTER<br>DUNMORE, PHD.</p>
  </section>

  <section class="cover cover--day">
    <h1>
      <span class="title-main">MEND THE</span>
      <span class="title-sub">QUIET HOURS</span>
    </h1>
    <div class="hearts">
      <div class="heart-slot" role="img" aria-label="Heart shattered into many pieces"></div>
      <div class="heart-slot" role="img" aria-label="Heart with pieces drawing back together"></div>
      <div class="heart-slot" role="img" aria-label="Heart whole with faint cracks"></div>
      <div class="heart-slot heart-slot--whole" role="img" aria-label="Fully mended heart"></div>
    </div>
    <p class="tagline">
      <span class="tagline-line tagline-line--one">For couples</span>
      <span class="tagline-line tagline-line--two">who <span class="emphasis">don't</span> want</span>
      <span class="tagline-line tagline-line--three">to break up</span>
    </p>
    <p class="authors">MARLA &amp; WALTER<br>DUNMORE, PHD.</p>
  </section>
</body>
</html>
```